Ashgrove Team Real Estate For Sale Signs

I have a few ideas and concepts of signs already done. The arch signs are 30 1/2" tall, 24" wide, and the arch begins at at 19 1/2". I am looking for a different set of ideas, fresh thoughts, to find something different, professional and eye catching. I have the current logo style guide, plus my eps files of what I have created. Not looking for a few logo...just something totally different. i dont want to use For Sale, was thinking You Next, Make It Yours, Home Awaits, Explore More, Find Home...

Target Market(s)

Real Estate BUYERS and setting an image for sellers to know quality

Industry/Entity Type

Residential Real Estate and Luxury Real Estate

Font styles to use
Other font styles liked:
• noted in style guide: Montserrat Bold

Requirements
Must have
• My Team Name (The Ashgrove Team) my logo (K) and HM logo. My colors are noted in the style guide. I am wanting to stand out from all competition BUT not be too busy. Somebody driving by only has a few seconds to read it. BELOW the sign, I will have 2 6x24" riders. One will have my name and photo, the other will have my phone number.
Nice to have
• These signs are going to be outside along streets to grab attention of drivers as passing the house.
Should not have
• I do not want any phone numbers on the sign.

```html
<!DOCTYPE html>
<html lang="en">
<head>
<meta charset="utf-8">
<title>The Ashgrove Team – Arch Sign Concepts</title>
<link rel="stylesheet" href="https://fonts.googleapis.com/css2?family=Montserrat:wght@600;700;800;900&display=swap">
<style>
  :root {
    --board: #939598;
    --ink: #111111;
    --paper: #ffffff;
    --brand-orange: #f26f23;
    --lockup-grey: #4a4a4a;
    --lockup-light: #bdbdbd;
  }
  html, body {
    margin: 0;
    width: 1200px;
    height: 896px;
    overflow: hidden;
    background: var(--board);
  }
  .presentation {
    display: block;
    width: 1200px;
    height: 896px;
    font-family: "Montserrat", Arial, sans-serif;
  }
  .headline { font-weight: 900; }
  .team-name { font-weight: 800; }
  .lockup-name { font-weight: 700; }
  .lockup-sub { font-weight: 600; }
  .variant-label { font-weight: 600; fill: var(--paper); }
</style>
</head>
<body>
<svg class="presentation" viewBox="0 0 1454 1086" xmlns="http://www.w3.org/2000/svg">
  <defs>
    <radialGradient id="sign-e-sheen" cx="50%" cy="50%" r="65%">
      <stop offset="0%" stop-color="#ffffff"/>
      <stop offset="60%" stop-color="#f1f1f2"/>
      <stop offset="100%" stop-color="#c4c5c7"/>
    </radialGradient>
    <clipPath id="arch-e">
      <path d="M109,935 V404 A296.5,296.5 0 0 1 702,404 V935 Z"/>
    </clipPath>
    <clipPath id="arch-f">
      <path d="M748,932 V404 A296,296 0 0 1 1340,404 V932 Z"/>
    </clipPath>
  </defs>

  <rect class="board" width="1454" height="1086" fill="var(--board)"/>

  <!-- Sign E: "You Next" -->
  <g class="sign sign-you-next" clip-path="url(#arch-e)">
    <rect x="109" y="100" width="593" height="835" fill="url(#sign-e-sheen)"/>

    <g class="team-mark">
      <text class="team-name" x="222" y="272" font-size="20" fill="var(--brand-orange)" transform="rotate(-90 222 272)">THE</text>
      <text class="team-name" x="232" y="272" font-size="56" fill="var(--ink)" textLength="378" lengthAdjust="spacingAndGlyphs">ASHGROVE</text>
      <text class="team-name" x="410" y="325" font-size="56" fill="var(--brand-orange)" text-anchor="middle">TEAM</text>
    </g>

    <polygon class="direction-arrow" points="109,415 493,415 493,348 680,521 493,694 493,627 109,627" fill="var(--brand-orange)"/>
    <text class="headline" x="210" y="500" font-size="122" fill="var(--paper)" textLength="282" lengthAdjust="spacingAndGlyphs">YOU</text>
    <text class="headline" x="237" y="598" font-size="122" fill="var(--paper)" textLength="338" lengthAdjust="spacingAndGlyphs">NEXT</text>

    <polygon class="corner-block" points="109,627 352,627 240,745" fill="var(--ink)"/>
    <polygon class="corner-block" points="548,770 702,910 702,935 430,935 415,905" fill="var(--ink)"/>
    <text class="team-name" x="375" y="775" font-size="30" fill="var(--ink)" text-anchor="middle" textLength="170" lengthAdjust="spacingAndGlyphs" transform="rotate(45 375 775)">ASHGROVE</text>

    <g class="brokerage-lockup">
      <text class="lockup-name" x="148" y="886" font-size="24" fill="var(--lockup-grey)" textLength="168" lengthAdjust="spacingAndGlyphs">HM CRESTLINE</text>
      <text class="lockup-sub" x="148" y="899" font-size="10" fill="var(--lockup-grey)">HALE MERIDIAN</text>
      <text class="lockup-sub" x="148" y="907" font-size="4.6" fill="var(--lockup-grey)">EACH OFFICE IS INDEPENDENTLY OWNED AND OPERATED</text>
    </g>
  </g>

  <!-- Sign F: "Explore More" -->
  <g class="sign sign-explore-more" clip-path="url(#arch-f)">
    <rect x="748" y="100" width="592" height="832" fill="var(--ink)"/>

    <polygon class="diagonal-rule" points="1264,206 1278,214 944,697 928,697" fill="var(--paper)"/>
    <g class="team-badge" transform="rotate(35 1050 320)">
      <rect x="955" y="225" width="190" height="190" fill="none" stroke="var(--paper)" stroke-width="12"/>
      <text class="team-name" x="1050" y="331" font-size="30" fill="var(--paper)" text-anchor="middle" textLength="148" lengthAdjust="spacingAndGlyphs">ASHGROVE</text>
    </g>

    <g class="team-mark">
      <text class="team-name" x="820" y="818" font-size="22" fill="var(--brand-orange)" textLength="32" lengthAdjust="spacingAndGlyphs" transform="rotate(-90 820 818)">THE</text>
      <text class="team-name" x="834" y="780" font-size="80" fill="var(--paper)" transform="rotate(-90 834 780)" textLength="460" lengthAdjust="spacingAndGlyphs">ASHGROVE</text>
      <text class="team-name" x="897" y="657" font-size="80" fill="var(--brand-orange)" transform="rotate(-90 897 657)" textLength="188" lengthAdjust="spacingAndGlyphs">TEAM</text>
    </g>

    <text class="headline" x="955" y="597" font-size="72" fill="var(--paper)" textLength="366" lengthAdjust="spacingAndGlyphs">EXPLORE</text>
    <text class="headline" x="1014" y="737" font-size="182" fill="var(--brand-orange)" textLength="306" lengthAdjust="spacingAndGlyphs">MO</text>
    <text class="headline" x="1014" y="907" font-size="182" fill="var(--brand-orange)" textLength="304" lengthAdjust="spacingAndGlyphs">RE</text>

    <g class="brokerage-lockup">
      <text class="lockup-name" x="787" y="880" font-size="24" fill="var(--lockup-light)" textLength="180" lengthAdjust="spacingAndGlyphs">HM CRESTLINE</text>
      <text class="lockup-sub" x="787" y="894" font-size="10" fill="var(--lockup-light)">HALE MERIDIAN</text>
      <text class="lockup-sub" x="787" y="904" font-size="4.6" fill="var(--lockup-light)">EACH OFFICE IS INDEPENDENTLY OWNED AND OPERATED</text>
    </g>
  </g>

  <text class="variant-label" x="391" y="1008" font-size="26" text-anchor="middle">E</text>
  <text class="variant-label" x="1046" y="1008" font-size="26" text-anchor="middle">F</text>
</svg>
</body>
</html>
```